Toys Packaging Design

Hello,

I am a toy brand company importing our toys from China and now I am rebranding my whole brand, including brand name change and logo and packaging designs, I have already a new brand name and logo (can be maybe revised).
Till now I really don’t have any good design so it's just like doing it from new,
I would like my brand should have a matching design for all our items so it looks professional,
Here are our items.
https://www.quorva.com/dp/Q7734KMZTA
https://www.quorva.com/dp/Q382NWDH5R
https://www.quorva.com/dp/Q06T8LPX2G

And here is our new items still not available on Quorva it will take just another about 2 days, but here you can see a few competitions links so maybe you can have an idea,
https://www.quorva.com/Dunko-3-Piece-Basketball-Playhouse-Toddlers/dp/Q93JXKP4WT/
https://www.quorva.com/Toddler-Basketball-Zippered-Toddlers-Included/dp/Q51VRMC8HN
https://www.quorva.com/Rocket-Ship-Play-Tent-Spaceship/dp/Q28LKDW7YE

Now the job is packaging for all of them, will begin with our princess play tent which till now it has A round poly bag size 31 cm by 41 cm and on it is an 8.5 x 11 designer paper, but from now on I would like to have A full designed round plastic bag (on both sides), about 31 cm by 41 cm,
Next will be our beach toys and balls designs which are just a round paper label which are about 4 x 4 inches.
Then we will go to the other items so this is really a nice and long job for all our packaging, also more to come.
I do not have any info to give you except the UPC meaning to say a part of the job is to take the info from the Quorva page or competitors or you can think by yourself or take a writer or any kids for images, just you should create a plan and tell me plan and price.
IN THE MEANTIME I WILL HAVE OTHER JOBS AS WELL LIKE INSERTS AND SO ON,

ALSO, I WILL NEED A WEBSITE...

• our first focus now is the Princess play tent round diameter of about 31 cm by 41 cm,
• I have added this because I got 1 design on the beach toys, which have 2 problems
• 1)Beach toys is not number one 2)Beach toys will not be a full page

```html
<!DOCTYPE html>
<html lang="en">
<head>
<meta charset="utf-8">
<title>Joybrook Princess Play Tent – Round Bag Packaging</title>
<link rel="stylesheet" href="https://fonts.googleapis.com/css2?family=Saira:wght@300;400;500;600;700&family=Pacifico&display=swap">
<style>
  :root{
    --bg:#fcd3ef;
    --ring:#ff6cc9;
    --ring-dark:#e63fae;
    --band:#fdaae6;
    --white:#ffffff;
    --pink-text:#ee4fb4;
    --star:#fc8fd6;
    --star-faint:#fde0f4;
    --brand:#7a2b8e;
    --label:#e94fb5;
    --tent-top:#e8359f;
    --tent-body:#f7c4e4;
  }
  *{box-sizing:border-box;margin:0;padding:0}
  html,body{width:1200px;height:1200px;overflow:hidden;background:var(--bg)}
  body{font-family:"Saira",sans-serif}
  .canvas{position:relative;width:1200px;height:1200px;background:var(--bg)}

  .bag-outer{position:absolute;background:var(--ring);border-radius:50%/40%}
  .bag-inner{position:absolute;background:var(--white);border:6px solid var(--ring-dark);border-radius:50%/40%;overflow:hidden}
  .bag-band{position:absolute;left:0;right:0;bottom:0;background:var(--band)}

  .front .bag-outer{left:30px;top:58px;width:559px;height:738px}
  .front .bag-inner{left:58px;top:84px;width:503px;height:684px}
  .front .bag-band{top:497px}

  .back .bag-outer{left:616px;top:329px;width:560px;height:737px}
  .back .bag-inner{left:644px;top:355px;width:504px;height:685px}
  .back .bag-band{top:496px}

  .logo-tab{position:absolute;left:199px;top:76px;width:219px;height:182px;background:var(--white);
    border:7px solid var(--ring-dark);border-top:none;border-radius:0 0 110px 110px;z-index:3;
    display:flex;flex-direction:column;align-items:center;justify-content:center;padding-top:10px;gap:10px}
  .brand-dot{width:34px;height:34px;border-radius:50%;background:var(--ring)}
  .brand-name{font-family:"Saira",sans-serif;font-weight:700;font-size:28px;color:var(--brand);letter-spacing:1px;line-height:1}

  .stars{position:absolute;left:0;top:0;width:1200px;height:1200px;z-index:2;pointer-events:none}

  .features{position:absolute;left:84px;top:373px;list-style:none;z-index:3}
  .features li{display:flex;align-items:center;gap:7px;height:41px;font-size:14.5px;font-weight:500;color:var(--pink-text)}
  .features svg{width:15px;height:15px;fill:var(--pink-text)}

  .product-photo{position:absolute;left:302px;top:246px;width:230px;height:317px;z-index:3;
    border-radius:50% 50% 40% 40%/45% 45% 20% 20%;
    background:linear-gradient(180deg,var(--tent-top) 0%,var(--tent-top) 38%,var(--tent-body) 40%,#f3b3dc 100%)}
  .castle-art{position:absolute;z-index:3;background:var(--band);border-radius:4px 4px 0 0}
  .front .castle-art{left:72px;top:520px;width:182px;height:68px}
  .back .castle-art{left:947px;top:790px;width:186px;height:68px}

  .product-title{position:absolute;left:104px;top:586px;z-index:3;color:var(--white);line-height:1}
  .product-title .script{display:block;font-family:"Pacifico",cursive;font-size:44px}
  .product-title .plain{display:block;font-weight:300;font-size:31px;margin-left:56px;margin-top:-4px}
  .product-blurb{position:absolute;left:329px;top:606px;width:178px;z-index:3;color:var(--white);font-size:7.6px;font-weight:600;line-height:10.7px}
  .product-size{position:absolute;left:208px;top:702px;width:200px;z-index:3;text-align:center;color:var(--white);font-size:14px;line-height:20px}
  .product-size .dims{font-size:15px}

  .side-label{position:absolute;width:300px;text-align:center;color:var(--label);font-size:44px;font-weight:400;line-height:1}
  .front .side-label{left:155px;top:828px}
  .back .side-label{left:745px;top:1097px}

  .back-brand{position:absolute;left:795px;top:418px;width:200px;text-align:center;z-index:3}
  .back-brand .brand-name{font-size:17px}
  .copy{position:absolute;left:734px;width:324px;z-index:3;text-align:center;color:var(--pink-text);font-size:7.4px;font-weight:500;line-height:10.7px}
  .copy p+p{margin-top:10.7px}
  .copy-top{top:458px}
  .copy-bottom{top:656px}
  .warning{position:absolute;left:690px;top:873px;width:412px;z-index:3;text-align:center;color:var(--white);font-size:6.4px;font-weight:500;line-height:9px}
</style>
</head>
<body>
<div class="canvas">
  <svg width="0" height="0" style="position:absolute">
    <defs>
      <symbol id="star" viewBox="-1 -1 2 2">
        <polygon points="0,-1 0.265,-0.364 0.951,-0.309 0.428,0.139 0.588,0.809 0,0.45 -0.588,0.809 -0.428,0.139 -0.951,-0.309 -0.265,-0.364"/>
      </symbol>
    </defs>
  </svg>

  <section class="front">
    <div class="bag-outer"></div>
    <div class="bag-inner"><div class="bag-band"></div></div>
    <div class="logo-tab"><span class="brand-dot"></span><span class="brand-name">JOYBROOK</span></div>

    <ul class="features">
      <li><svg viewBox="-1 -1 2 2"><use href="#star"/></svg>Glow in the Dark Stars</li>
      <li><svg viewBox="-1 -1 2 2"><use href="#star"/></svg>Indoor &amp; Outdoor Use</li>
      <li><svg viewBox="-1 -1 2 2"><use href="#star"/></svg>Quick And Easy To Assemble</li>
    </ul>

    <div class="product-photo" role="img" aria-label="Product photo of the pink princess castle play tent with pointed roof and open door"></div>
    <div class="castle-art" role="img" aria-label="Pink castle silhouette illustration"></div>

    <h1 class="product-title"><span class="script">Princess</span><span class="plain">play tent</span></h1>
    <p class="product-blurb">Princess Play tent creates a kingdom in any corner of the house with this magical castle for kids. This charming castle has two side windows for ventilation and enough room for 2-3 little princesses to play</p>
    <div class="product-size"><div>Size</div><div class="dims">41.5″ x 41.5″ x 54″</div></div>
    <div class="side-label">Front</div>
  </section>

  <section class="back">
    <div class="bag-outer"></div>
    <div class="bag-inner"><div class="bag-band"></div></div>
    <div class="castle-art" role="img" aria-label="Pink castle silhouette illustration"></div>

    <div class="back-brand"><span class="brand-name">JOYBROOK</span></div>

    <div class="copy copy-top">
      <p>Welcome to the royal castle! This princess play tent gives every little girl a cozy hideaway of her own. The soft pink walls and pointed roof turn any bedroom, playroom or backyard into a fairy tale kingdom. Glow in the dark stars shine at night for magical bedtime stories. Two mesh side windows keep fresh air flowing, while the roll-up door ties open for easy access. Sturdy flexible rods hold their shape through hours of play.</p>
      <p>Setup takes only minutes. Simply pop the tent open, secure the flexible frame and your castle is ready. When playtime is over, it folds flat into the included carry bag for easy storage or travel to grandma's house, the park or a sleepover with friends.</p>
    </div>
    <div class="copy copy-bottom">
      <p>Made for imagination. Little princesses can host tea parties, read picture books, play dress up or share secrets with their best friends inside. The roomy interior fits two to three children at once, so siblings and playmates can join the fun. Durable polyester fabric wipes clean with a damp cloth, and the bright colors stay cheerful wash after wash. It makes a wonderful gift for birthdays, holidays and every special day in between.</p>
      <p>Package includes one princess castle tent, one set of flexible rods and one carry bag. Recommended for ages three and up. Adult assembly required. Always supervise young children during play and keep the tent away from fire, heaters and sharp objects.</p>
    </div>
    <p class="warning">Warning: choking hazard. Small parts. Not for children under three years. This bag is not a toy; keep it away from babies and young children to avoid danger of suffocation. Remove all packaging before giving the tent to a child. Use only on flat, dry ground and never near open flames. Check rods and seams regularly and stop using the tent if any part is damaged. Store in a cool dry place. Made in China. Please keep this information for future reference.</p>
    <div class="side-label">Back</div>
  </section>

  <svg class="stars" viewBox="0 0 1200 1200" aria-hidden="true">
    <g fill="var(--star)">
      <use href="#star" x="153" y="209" width="20" height="20"/>
      <use href="#star" x="439" y="181" width="28" height="28"/>
      <use href="#star" x="86" y="274" width="14" height="14"/>
      <use href="#star" x="213" y="268" width="14" height="14"/>
      <use href="#star" x="349" y="270" width="10" height="10"/>
      <use href="#star" x="487" y="242" width="12" height="12"/>
      <use href="#star" x="146" y="311" width="30" height="30"/>
      <use href="#star" x="289" y="310" width="24" height="24"/>
      <use href="#star" x="512" y="314" width="24" height="24"/>
      <use href="#star" x="275" y="419" width="10" height="10"/>
    </g>
    <g fill="var(--star-faint)">
      <use href="#star" x="827" y="435" width="24" height="24"/>
      <use href="#star" x="1028" y="445" width="24" height="24"/>
      <use href="#star" x="674" y="544" width="14" height="14"/>
      <use href="#star" x="1075" y="513" width="10" height="10"/>
      <use href="#star" x="1099" y="584" width="24" height="24"/>
      <use href="#star" x="946" y="442" width="10" height="10"/>
    </g>
  </svg>
</div>
</body>
</html>
```